Zielgruppe
Wir sind eine Lebküchnerei und möchten einen Flyer in 6-seitigen Wickelfalz Format. Unsere Zielgruppe sind mittelständische Unternehmen in ganz Deutschland.
Der Flyer soll einen ersten Eindruck auf unsere Produktvielfalt und die hohe Qualität der Lebkuchen vermitteln.
Aufgabenstellung
Passend zu unserer Website (Hintergrundfarbe RGB: Farbt: 30 Rot 255, Sätt. 240 Grün 208, Hell 151 Blau 66 HEX: FFD047) und Logo sollen Farbelemente in Gold und dunklem Rot zu finden sein. Daten bitte aus den angehängten Materialbild bzw. unserer Website (www.gebaeck-hornberg.de - wird gerade neu überarbeitet) entnehmen.
Unsere Produkte sind: Lebkuchen Konfekt, Lebkuchen als 3er oder 5er verpackt (sortenrein und sortiert), Walnuss-, Rum-Traube-Nuss- & Pistazienlebkuchen (jeweils 3er verpackt, nur sortenrein) sowie einzeln verpackte Lebkuchen und Geschenkdosen (verschiedene).
z. B. Vorderseite: unser Logo mit Webadresse, evtl. Lebkuchenbild Image; Rückseite: Kontakt und Standortinformationen
Wir bevorzugen mehrere Fotos, angehängte Fotos sollen als Beispiel dienen, Neuere sind in Bearbeitung und sollen später eingefügt/ersetzt werden.

```html
<!DOCTYPE html>
<html lang="de">
<head>
<meta charset="utf-8">
<title>Hornberg Lebkuchen – Wickelfalz-Flyer</title>
<link rel="stylesheet" href="https://fonts.googleapis.com/css2?family=Marcellus&family=Crimson+Pro:wght@400;600;700&display=swap">
<style>
:root{
  --red:#a00b0b;
  --red-deep:#7e0606;
  --gold:#e7c04a;
  --gold-light:#f4dc86;
  --gold-dark:#b98a1c;
  --cream:#fff8e6;
  --page:#ffffff;
  --photo-warm:#c98a4e;
  --photo-shop:#b48c4c;
  --choc:#3b1e12;
  --gingerbread:#8a4b22;
}
*{box-sizing:border-box;margin:0;padding:0}
html,body{width:1200px;height:2705px;overflow:hidden;background:var(--page)}
body{position:relative;font-family:"Crimson Pro",Georgia,serif;color:var(--cream)}
.spread{position:absolute;left:72px;width:1040px;height:735px;background:var(--red);overflow:hidden;box-shadow:0 6px 22px rgba(0,0,0,.28)}
.spread--outside{top:420px}
.spread--inside{top:1560px}
.spread svg.bg{position:absolute;inset:0;width:100%;height:100%}
.headline{position:absolute;font-family:"Marcellus",Georgia,serif;color:var(--gold);font-weight:400;line-height:1.05}
.body-copy{position:absolute;font-size:16.5px;line-height:1.1;text-align:center;color:#fff}
.divider{position:absolute;height:1px;background:var(--gold)}
.address{position:absolute;font-size:15.5px;line-height:1.15;color:#fff}
.site-url{position:absolute;font-weight:700;color:var(--gold);font-size:17px}
.brand-badge{position:absolute;display:flex;align-items:center;gap:8px;background:#fff;border:2px solid var(--gold);border-radius:40px;padding:6px 14px 6px 8px;font-family:"Crimson Pro",serif;font-weight:700;font-size:20px;color:var(--red)}
.brand-badge .dot{width:26px;height:26px;border-radius:50%;background:var(--gold)}
.label{position:absolute;font-weight:700;font-size:17px;color:var(--gold)}
.list{position:absolute;list-style:none;font-size:15px;line-height:1.2;color:var(--gold-light)}
.list li::before{content:"• ";color:var(--gold-light)}
.sub{position:absolute;font-size:15px;color:var(--gold-light)}
</style>
</head>
<body>

<!-- Außenseite -->
<section class="spread spread--outside">
  <svg class="bg" viewBox="0 0 1040 735" aria-hidden="false">
    <defs>
      <linearGradient id="warm" x1="0" y1="0" x2="1" y2="1">
        <stop offset="0" stop-color="#e0b07a"/><stop offset=".55" stop-color="#a9602e"/><stop offset="1" stop-color="#dba46a"/>
      </linearGradient>
      <linearGradient id="shop" x1="0" y1="0" x2="0" y2="1">
        <stop offset="0" stop-color="#8b6a3a"/><stop offset=".5" stop-color="#d6ad62"/><stop offset="1" stop-color="#7a5a38"/>
      </linearGradient>
    </defs>
    <path role="img" aria-label="Foto: Verkaufstheke der Bäckerei mit Kunden und Personal" d="M0 0H340V390C260 395 200 370 120 330 70 305 30 290 0 290Z" fill="url(#shop)"/>
    <path d="M0 290C30 290 70 305 120 330 200 370 260 395 340 390" fill="none" stroke="var(--gold)" stroke-width="4"/>
    <path role="img" aria-label="Foto: Elisenlebkuchen mit Mandeln und Schokoladenglasur, Sternanis und Nüssen" d="M340 0H1040V600C960 600 880 590 820 530 760 470 730 390 660 380 560 370 460 395 340 390Z" fill="url(#warm)"/>
    <path d="M340 390C460 395 560 370 660 380 730 390 760 470 820 530 880 590 960 600 1040 600" fill="none" stroke="var(--gold)" stroke-width="4"/>
    <path d="M840 0H1040V150C1010 130 990 140 960 120 930 100 900 110 880 80 860 50 840 40 840 0Z" fill="#fff"/>
  </svg>

  <div class="brand-badge" style="left:870px;top:40px"><span class="dot"></span>Hornberg</div>
  <div class="brand-badge" style="left:410px;top:330px"><span class="dot"></span>Hornberg</div>

  <h2 class="headline" style="left:65px;top:405px;font-size:50px">Über uns</h2>
  <p class="body-copy" style="left:30px;top:475px;width:290px">Wir produzieren nur erlesenste Back­waren. Unsere originalen Elisenlebkuchen sind weit über die Grenzen Nürnbergs und Fürths bekannt. Sie werden u. a. in einigen ausgesuchten Spezialitäten- und Schokoladen Fachgeschäften in ganz Bayern verkauft.<br><br>Darauf sind wir besonders stolz. Sehr beliebt ist auch unser Elisenlebkuchen­konfekt.</p>

  <h2 class="headline" style="left:420px;top:475px;font-size:50px">Kontakt</h2>
  <p class="body-copy" style="left:345px;top:560px;width:335px">www.gebaeck-hornberg.de<br>post@baeckerei-hornberg.de</p>
  <div class="divider" style="left:345px;top:603px;width:330px"></div>
  <p class="address" style="left:372px;top:620px;text-align:right">Hauptsitz Fürth<br>Lindenstraße 14<br>90762 Fürth<br>Tel:&nbsp; 0911 550132</p>
  <p class="address" style="left:525px;top:620px">Ahornweg 8<br>Ecke Birkenstraße<br>90471 Nürnberg<br>Tel: 0911 4402817</p>
  <span class="site-url" style="left:770px;top:686px">www.gebaeck-hornberg.de</span>
</section>

<!-- Innenseite -->
<section class="spread spread--inside">
  <svg class="bg" viewBox="0 0 1040 735">
    <defs>
      <linearGradient id="warm2" x1="0" y1="0" x2="1" y2="1">
        <stop offset="0" stop-color="#d9a772"/><stop offset=".6" stop-color="#9c5628"/><stop offset="1" stop-color="#e2b57c"/>
      </linearGradient>
      <radialGradient id="disc" cx=".45" cy=".4" r=".6">
        <stop offset="0" stop-color="#c58a3c"/><stop offset="1" stop-color="#7a2a0c"/>
      </radialGradient>
    </defs>
    <path role="img" aria-label="Foto: Lebkuchen, Schokolade, Zimtstangen und Gewürze" d="M560 0H1040V320C940 330 840 280 760 210 690 140 620 70 560 0Z" fill="url(#warm2)"/>
    <path d="M560 0C620 70 690 140 760 210 840 280 940 330 1040 320" fill="none" stroke="var(--gold)" stroke-width="4"/>
    <path role="img" aria-label="Foto: Lebkuchen mit Zutaten wie Honig, Zitronat, Orangeat und Nüssen" d="M0 445C140 440 260 500 340 580 400 640 440 700 490 735H0Z" fill="url(#warm2)"/>
    <path d="M0 445C140 440 260 500 340 580 400 640 440 700 490 735" fill="none" stroke="var(--gold)" stroke-width="4"/>

    <g fill="none" stroke="var(--gold)" stroke-width="1.2">
      <polyline points="210,62 455,62 500,325"/>
      <polyline points="40,285 255,285 440,355"/>
      <polyline points="975,450 720,450 620,375"/>
      <polyline points="485,495 515,590 930,590"/>
    </g>
    <g fill="var(--red)" stroke="var(--gold)" stroke-width="1.2">
      <circle cx="210" cy="62" r="3"/><circle cx="40" cy="285" r="3"/><circle cx="975" cy="450" r="3"/><circle cx="930" cy="590" r="3"/>
    </g>

    <circle cx="533" cy="410" r="88" fill="url(#disc)" stroke="var(--gold)" stroke-width="4"/>

    <g role="img" aria-label="Foto: Lebkuchenkonfekt">
      <circle cx="410" cy="145" r="62" fill="var(--choc)"/>
    </g>
    <g role="img" aria-label="Foto: drei Lebkuchen sortenrein">
      <circle cx="285" cy="290" r="40" fill="var(--choc)"/>
      <circle cx="255" cy="365" r="40" fill="var(--gingerbread)"/>
      <circle cx="335" cy="365" r="40" fill="#6b3a20"/>
    </g>
    <g role="img" aria-label="Foto: fünf Lebkuchen sortiert">
      <circle cx="770" cy="250" r="40" fill="#6b3a20"/>
      <circle cx="860" cy="250" r="40" fill="var(--choc)"/>
      <circle cx="730" cy="330" r="40" fill="var(--gingerbread)"/>
      <circle cx="815" cy="330" r="40" fill="var(--choc)"/>
      <circle cx="900" cy="330" r="40" fill="#7d5a3c"/>
    </g>
    <g role="img" aria-label="Foto: rote Geschenkdosen mit winterlichem Muster">
      <rect x="735" y="525" width="105" height="150" rx="10" fill="#b81c22"/>
      <rect x="800" y="555" width="115" height="150" rx="10" fill="#c8242a"/>
    </g>
  </svg>

  <h2 class="headline" style="left:38px;top:82px;font-size:50px">Unsere<br>Produkte</h2>

  <span class="label" style="left:212px;top:38px">Lebkuchen als Konfekt</span>

  <span class="label" style="left:50px;top:262px">3er Lebkuchen sortenrein</span>
  <ul class="list" style="left:50px;top:292px"><li>Walnuss</li><li>Rum-Traube-Nuss</li><li>Pistazien</li></ul>

  <span class="label" style="left:858px;top:426px">5er Lebkuchen</span>
  <span class="sub" style="left:825px;top:458px">sortenrein und sortiert</span>

  <span class="label" style="left:543px;top:566px">Geschenkdosen</span>
  <ul class="list" style="left:533px;top:598px"><li>Walnuss</li><li>Rum-Traube-Nuss</li><li>Pistazien</li></ul>
</section>

</body>
</html>
```